Kettle Ledger Business Card design

We need a stand out business card design for Accounting practice based in Australia specialising in pubs, clubs and hotels. We help venues maximise margins, create time and manage cashflow. One club we have been working with for the last 6 months has increased revenue by 3% and margin by 5% in this time frame. We have a back office outsourced system that costs less than having a full time employee and also allows the venues the added benefit of:<br/>-using the office space to become a revenue generating opportunity. <br/>-a complete system to enhance governance, accountability and efficiency within their operation<br/>-52 weeks cover so no hassle to cover annual/sick .. leave<br/><br/>We would like to see designs that use the colours of our logo (green & blue).
Target Market(s)
Australian Pubs, Clubs & Hotels abookkeeping, accounting and tax services
Industry/Entity Type
Accountant
Contact Information for Business Card
Miriam Oakley CPA
Principal
Accountant Tax Agent
Miriam@KettleLedger-example.com.au
0418693142
www.kettleledger-example.com.au
Accounting / Payroll / Tax / SMSF / Technology
Colors
Designer to choose colors to be used in the design.
Look and feel
Each slider illustrates characteristics of the customer's brand and the style your logo design should communicate.

```html
<!DOCTYPE html>
<html lang="en">
<head>
<meta charset="utf-8">
<title>Kettle Ledger Business Card</title>
<link rel="stylesheet" href="https://fonts.googleapis.com/css2?family=Roboto:wght@400;500;700&display=swap">
<style>
  :root {
    --brand-blue: #1f3a8f;
    --brand-green: #0f6b3a;
    --text-grey: #6b6b6b;
    --card-white: #ffffff;
    --card-black: #111111;
    --backdrop: #e8e5e0;
  }
  * { box-sizing: border-box; margin: 0; padding: 0; }
  html, body {
    width: 1200px; height: 1200px; overflow: hidden;
    background: var(--backdrop);
    font-family: "Roboto", Arial, sans-serif;
  }
  .canvas { position: relative; width: 1200px; height: 1200px; }
  .card {
    position: absolute; left: 214px; width: 771px; height: 440px;
    box-shadow: 0 4px 14px rgba(0,0,0,0.18);
  }
  .card--front { top: 140px; background: var(--card-white); }
  .card--back { top: 625px; background: var(--card-black); }

  .brand {
    position: absolute; display: flex; align-items: center;
  }
  .brand__dot { border-radius: 50%; background: var(--brand-green); flex: none; }
  .brand__name {
    color: var(--brand-blue); font-weight: 700; white-space: nowrap; letter-spacing: -0.5px;
  }
  .card--front .brand { left: 36px; top: 190px; gap: 14px; }
  .card--front .brand__dot { width: 46px; height: 46px; }
  .card--front .brand__name { font-size: 34px; }

  .divider {
    position: absolute; left: 386px; top: 131px; width: 2px; height: 180px;
    background: var(--brand-green);
  }
  .contact { position: absolute; left: 421px; top: 126px; }
  .contact__name { font-size: 27px; font-weight: 500; color: var(--brand-blue); line-height: 1.1; }
  .contact__post { color: var(--brand-green); font-weight: 400; }
  .contact__role { font-size: 20px; color: var(--text-grey); line-height: 1.22; margin-top: 6px; }
  .contact__list { list-style: none; margin-top: 24px; }
  .contact__item {
    display: flex; align-items: center; gap: 7px;
    font-size: 18px; color: var(--text-grey); line-height: 27px;
  }
  .contact__icon { width: 16px; height: 16px; flex: none; fill: var(--brand-blue); }

  .card--back .brand { left: 50%; top: 170px; transform: translateX(-50%); gap: 22px; }
  .card--back .brand__dot { width: 84px; height: 84px; }
  .card--back .brand__name { font-size: 58px; }

  .services {
    position: absolute; left: 0; right: 0; top: 384px; text-align: center;
    font-size: 19px; color: var(--brand-blue);
  }
  .services__sep { color: var(--brand-green); margin: 0 9px; font-size: 14px; vertical-align: 2px; }
</style>
</head>
<body>
<main class="canvas">
  <section class="card card--front">
    <div class="brand">
      <span class="brand__dot"></span>
      <span class="brand__name">Kettle Ledger</span>
    </div>
    <div class="divider"></div>
    <div class="contact">
      <p class="contact__name">Miriam Oakley <span class="contact__post">CPA</span></p>
      <p class="contact__role">Principal<br>Accountant Tax Agent</p>
      <ul class="contact__list">
        <li class="contact__item">
          <svg class="contact__icon" viewBox="0 0 24 24" aria-hidden="true"><path d="M6.6 10.8a15.1 15.1 0 0 0 6.6 6.6l2.2-2.2c.3-.3.7-.4 1-.2 1.1.4 2.3.6 3.6.6.6 0 1 .4 1 1V20c0 .6-.4 1-1 1A17 17 0 0 1 3 4c0-.6.4-1 1-1h3.5c.6 0 1 .4 1 1 0 1.3.2 2.5.6 3.6.1.3 0 .7-.2 1z"/></svg>
          0418 693 142
        </li>
        <li class="contact__item">
          <svg class="contact__icon" viewBox="0 0 24 24" aria-hidden="true"><path d="M2 5h20v14H2z" opacity="0"/><path d="M2 5h20v1.2l-10 6.3L2 6.2zM2 8.6l10 6.3 10-6.3V19H2z"/></svg>
          Miriam@KettleLedger-example.com.au
        </li>
        <li class="contact__item">
          <svg class="contact__icon" viewBox="0 0 24 24" aria-hidden="true"><path d="M12 2a10 10 0 1 0 0 20 10 10 0 0 0 0-20zm6.9 6h-3a15.6 15.6 0 0 0-1.3-3.6A8 8 0 0 1 18.9 8zM12 4c.8 1.2 1.5 2.5 1.9 4h-3.8c.4-1.5 1.1-2.8 1.9-4zM4.3 14a8 8 0 0 1 0-4h3.4a16.5 16.5 0 0 0 0 4zm.8 2h3a15.6 15.6 0 0 0 1.3 3.6A8 8 0 0 1 5.1 16zm3-8h-3a8 8 0 0 1 4.3-3.6C8.8 5.6 8.4 6.8 8.1 8zM12 20c-.8-1.2-1.5-2.5-1.9-4h3.8c-.4 1.5-1.1 2.8-1.9 4zm2.3-6H9.7a14.7 14.7 0 0 1 0-4h4.6a14.7 14.7 0 0 1 0 4zm.3 5.6c.6-1.1 1-2.3 1.3-3.6h3a8 8 0 0 1-4.3 3.6zm1.7-5.6a16.5 16.5 0 0 0 0-4h3.4a8 8 0 0 1 0 4z"/></svg>
          www.kettleledger-example.com.au
        </li>
      </ul>
    </div>
  </section>

  <section class="card card--back">
    <div class="brand">
      <span class="brand__dot"></span>
      <span class="brand__name">Kettle Ledger</span>
    </div>
    <p class="services">
      Accounting<span class="services__sep">•</span>Payroll<span class="services__sep">•</span>Tax<span class="services__sep">•</span>SMSF<span class="services__sep">•</span>Technology
    </p>
  </section>
</main>
</body>
</html>
```